Brookvale Systems Yellow rose letterhead

I have a new logo for my company but in its current form it is too large to be used on letterhead or as a email signature. I need to have the designer use elements from the current logo and create something close to the original but more suited for smaller items.
Updates

I just uploaded a copy of our logo that does not have the weathered affect. Thanks

Industry/Entity Type

It Company

Requirements
Must have
• The design must maintain the visual effect of the current logo. It needs to include the yellow rose and the name of the company.
Nice to have
• It would be nice to maintain the stamp theme and incorporate my name, address, phone, email. etc.

```html
<!DOCTYPE html>
<html lang="en">
<head>
<meta charset="utf-8">
<title>Brookvale Systems Letterhead</title>
<link rel="stylesheet" href="https://fonts.googleapis.com/css2?family=Source+Sans+3:wght@400;700&family=Archivo+Black&display=swap">
<style>
  :root {
    --paper: #ffffff;
    --sun: #fbc814;
    --aqua-soft: #c7e9ed;
    --aqua: #86d3d9;
    --ink: #1a1a1a;
  }
  * { margin: 0; padding: 0; box-sizing: border-box; }
  html, body { width: 848px; height: 1200px; overflow: hidden; background: var(--paper); }
  .letterhead { position: relative; width: 848px; height: 1200px; background: var(--paper); font-family: "Source Sans 3", sans-serif; color: var(--ink); overflow: hidden; }
  .artwork { position: absolute; inset: 0; width: 848px; height: 1200px; }
  .brand { position: absolute; left: 26px; top: 26px; display: flex; align-items: center; gap: 18px; }
  .brand-dot { width: 92px; height: 92px; border-radius: 50%; background: var(--sun); }
  .brand-name { font-family: "Source Sans 3", sans-serif; font-weight: 700; font-size: 32px; line-height: 1.05; color: var(--aqua); letter-spacing: 1px; }
  .sender { position: absolute; left: 34px; top: 1078px; font-size: 16px; line-height: 20.5px; font-style: normal; }
  .tagline { position: absolute; left: 612px; top: 1117px; width: 220px; text-align: center; font-family: "Archivo Black", sans-serif; }
  .tagline-title { font-size: 12.5px; letter-spacing: 0.6px; line-height: 15px; }
  .tagline-sub { font-size: 9px; line-height: 12px; }
</style>
</head>
<body>
<div class="letterhead">
  <svg class="artwork" viewBox="0 0 595 842" preserveAspectRatio="none" aria-hidden="true">
    <g class="sweep" fill="var(--aqua-soft)">
      <path d="M595 22 C470 110 400 300 407 470 C413 620 475 720 580 802 L592 794 C500 720 438 610 427 470 C420 310 490 130 595 42 Z"/>
      <path d="M595 40 C520 130 478 280 492 380 C503 450 546 510 595 545 Z"/>
    </g>
    <path class="sweep-line" d="M586 12 C455 95 385 300 393 470 C400 620 460 710 545 775" fill="none" stroke="var(--aqua-soft)" stroke-width="1.2"/>
    <rect class="footer-band" x="0" y="734" width="595" height="108" fill="var(--sun)"/>
    <path class="sweep-tail" d="M522 734 C545 757 565 778 580 802 L592 794 C578 774 560 754 538 734 Z" fill="var(--aqua-soft)" opacity="0.75"/>
  </svg>

  <header class="brand">
    <div class="brand-dot"></div>
    <div class="brand-name">Brookvale<br>Systems</div>
  </header>

  <address class="sender">
    Maren Holloway, PhD<br>
    214 Cedar Ridge Lane, Ste 1180<br>
    Willow Falls, TX 76510<br>
    maren@brookvale-systems.com<br>
    1-800-555-0147
  </address>

  <div class="tagline">
    <div class="tagline-title">THE SYSTEMS BUILDERS</div>
    <div class="tagline-sub">Designing Clear and<br>Reliable Business Software</div>
  </div>
</div>
</body>
</html>
```